Create a website in Wordpress for an interior design company

Create a website for our interior design company 'Dwellora'

-Color preferences - Neutral and warm colors. Nothing too bright
-Aesthetic: Modern, Minimalist, Classic, Mature, Luxury
-Mission Statement: Transforming homes into personalized dream spaces through exceptional interior design, meticulous attention to detail, and a touch of the unexpected.
-Brand Values: innovation, creativity, passion and sustainability

Examples: https://www.petrakinslowinteriors.com.au/
https://www.tavelcraftstudio.com/

About
Portfolio
Inquire page

```html
<!DOCTYPE html>
<html lang="en">
<head>
<meta charset="utf-8">
<title>Dwellora — Interior Design</title>
<link rel="stylesheet" href="https://fonts.googleapis.com/css2?family=Teko:wght@400;500;600&family=Playfair+Display:wght@500&family=Poppins:wght@400;500;600&display=swap">
<style>
:root{
  --gold:#b39a7b;
  --gold-dark:#a2896b;
  --ink:#1d1d1d;
  --body:#777;
  --cream:#f6f1ef;
  --dark:#1b1b1b;
  --footer:#26252e;
  --footer-text:#9a99a3;
  --white:#fff;
  --line:#e9e2e0;
}
*{margin:0;padding:0;box-sizing:border-box}
html,body{width:1200px;height:3113px;overflow:hidden}
body{position:relative;background:var(--white);font-family:"Poppins",sans-serif;color:var(--body)}
.abs{position:absolute}
.caps{font-family:"Teko",sans-serif;text-transform:uppercase}

/* hero */
.hero-photo{left:0;top:0;width:1200px;height:605px;background:linear-gradient(100deg,#c9b9a3 0%,#9c8a74 25%,#5e5246 45%,#4a4039 70%,#6f6457 100%)}
.hero-shade{left:360px;top:0;width:840px;height:605px;background:rgba(30,26,22,.35)}
.nav{top:30px;right:184px;display:flex;gap:24px;font-size:11px;font-weight:600;color:var(--white);letter-spacing:.5px}
.nav .active{color:var(--gold)}
.nav-social{top:27px;left:1058px;display:flex;gap:12px}
.dot{width:12px;height:12px;border-radius:50%;background:rgba(255,255,255,.85)}
.brand{font-family:"Poppins",sans-serif;font-weight:500;color:var(--white);font-size:22px}
.hero-brand{left:87px;top:38px}
.hero-kicker{left:240px;top:178px;color:var(--white);font-size:15px;letter-spacing:11px}
.hero-title{left:240px;top:206px;color:var(--white);font-size:62px;font-weight:600;letter-spacing:3px;line-height:1}
.hero-copy{left:240px;top:298px;width:480px;color:var(--white);font-size:13px;line-height:23px}
.hero-btn{left:268px;top:390px;color:var(--white);font-size:15px;letter-spacing:2px;padding-bottom:6px;border-bottom:1px solid rgba(255,255,255,.6)}
.counter{left:966px;top:112px;color:var(--white);font-size:34px}
.arrows{left:1124px;top:488px;width:44px;height:86px;border:1px solid rgba(255,255,255,.4)}
.arrows-line{left:999px;top:551px;width:201px;height:1px;background:rgba(255,255,255,.5)}

/* services */
.services{left:0;top:543px;width:999px;height:249px;background:var(--cream)}
.service{top:614px;width:260px}
.service-head{display:flex;align-items:center;gap:14px}
.service-num{font-family:"Teko",sans-serif;font-size:32px;color:var(--gold);letter-spacing:2px}
.service-rule{width:40px;height:1px;background:var(--gold)}
.service-name{font-size:14px;color:var(--gold);letter-spacing:3px}
.service p{margin-top:14px;font-size:12.5px;line-height:23px}

/* about */
.about-label{left:186px;top:902px;color:var(--gold);font-size:13px;letter-spacing:3px}
.about-title{left:186px;top:932px;font-family:"Playfair Display",serif;font-weight:500;font-size:35px;line-height:44px;color:var(--ink)}
.about-copy{left:186px;top:1036px;width:420px;font-size:13.5px;line-height:25px}
.about-tags{left:186px;top:1148px;display:flex;font-size:9px;letter-spacing:1.6px}
.about-tags span{padding:0 10px;border-left:1px solid #ddd}
.about-tags span:first-child{padding-left:0;border:0}
.btn{left:186px;top:1194px;width:126px;height:38px;background:var(--gold);color:var(--white);font-size:12.5px;font-weight:500;letter-spacing:.6px;display:flex;align-items:center;justify-content:center}
.photo-a{left:758px;top:870px;width:279px;height:208px;background:linear-gradient(135deg,#d8cdbf,#a9977f 60%,#e0c48a)}
.photo-b{left:608px;top:1095px;width:240px;height:173px;background:linear-gradient(135deg,#e6e3de,#b9b3aa 60%,#8a7d6a)}
.exp-box{left:871px;top:1095px;width:166px;height:173px;border:6px solid var(--cream)}
.exp-num{left:871px;top:1148px;font-family:"Teko",sans-serif;font-size:54px;font-weight:600;color:var(--ink);line-height:1}
.exp-label{left:871px;top:1210px;font-size:10px;color:var(--gold);letter-spacing:3px}

/* portfolio */
.portfolio{left:0;top:1362px;width:1200px;height:955px;background:var(--dark)}
.filter{left:639px;top:1436px;width:379px;height:44px;border-radius:22px;background:#222;display:flex;align-items:center;justify-content:center;gap:16px;font-size:9.5px;letter-spacing:1.2px;color:#aaa}
.filter .on{color:#6fd3b0;font-weight:600}
.filter i{width:5px;height:5px;border-radius:50%;background:#6fd3b0}
.port-line{left:0;top:1704px;width:1200px;height:1px;background:rgba(255,255,255,.25)}
.work-title{width:352px;text-align:center;font-size:15px;letter-spacing:3.5px;color:var(--gold);font-weight:500}
.work-sub{width:352px;text-align:center;font-size:11px;letter-spacing:2px;color:var(--gold-dark)}

/* contact */
.map{left:0;top:2317px;width:599px;height:469px;background:linear-gradient(160deg,#eeeeee,#dcdcdc 55%,#e8e8e8)}
.contact-title{left:713px;top:2396px;font-family:"Playfair Display",serif;font-size:26px;color:var(--ink)}
.contact-kicker{left:713px;top:2444px;font-size:13px;color:var(--gold);letter-spacing:4px}
.contact-line{left:713px;font-size:13px;letter-spacing:1px;color:var(--body)}
.contact-head{left:713px;top:2577px;font-size:14px;letter-spacing:4px;color:var(--ink);font-weight:600}
.contact-social{left:713px;top:2665px;display:flex;gap:8px}
.contact-social span{width:33px;height:33px;border-radius:50%;background:#f1f1f1}

/* footer */
.footer{left:0;top:2786px;width:1200px;height:327px;background:var(--footer)}
.foot-brand{left:155px;top:2852px}
.foot-copy{left:155px;top:2898px;width:220px;font-size:11px;line-height:16px;color:var(--footer-text)}
.foot-social{left:155px;top:2956px;display:flex;gap:7px}
.foot-social span{width:24px;height:24px;border-radius:50%;border:1px solid #555;position:relative}
.foot-social span::after{content:"";position:absolute;left:8px;top:8px;width:6px;height:6px;border-radius:50%;background:#ddd}
.foot-head{top:2846px;font-size:10px;letter-spacing:1.5px;color:var(--gold);font-weight:500}
.foot-head::after{content:"";display:inline-block;width:90px;height:1px;background:#3b3a45;vertical-align:middle;margin-left:10px}
.foot-list{list-style:none;font-size:11px;color:#e6e6ea}
.foot-list li{height:33px}
.foot-list li::before{content:"›";color:var(--gold);margin-right:9px}
.foot-text{font-size:10.5px;color:var(--footer-text);line-height:16px}
.foot-bottom{top:3080px;font-size:10.5px;color:var(--footer-text)}
.foot-bottom b{color:#d0d0d6;font-weight:600}
.foot-nav{left:903px;top:3080px;display:flex;gap:14px;font-size:10.5px;color:var(--footer-text)}
.foot-nav i{width:1px;height:12px;background:#555}
</style>
</head>
<body>

<header>
  <div class="abs hero-photo" role="img" aria-label="Warm modern living and dining room interior with pendant lights and marble wall"></div>
  <div class="abs hero-shade"></div>
  <div class="abs brand hero-brand">Dwellora</div>
  <nav class="abs nav"><span class="active">HOME</span><span>ABOUT</span><span>SERVICES</span><span>PROJECTS</span><span>CONTACT</span></nav>
  <div class="abs nav-social"><span class="dot"></span><span class="dot"></span><span class="dot"></span><span class="dot"></span></div>
  <div class="abs caps hero-kicker">Welcome to</div>
  <h1 class="abs caps hero-title">Dwellora</h1>
  <p class="abs hero-copy">Transforming homes into personalized dream spaces through exceptional interior design, meticulous attention to detail, and a touch of the unexpected.</p>
  <div class="abs caps hero-btn">Get in touch</div>
  <div class="abs caps counter">1 , 3</div>
  <div class="abs arrows">
    <svg width="44" height="86" viewBox="0 0 44 86"><path d="M18 24l4-4 4 4M18 60l4 4 4-4" stroke="#fff" stroke-width="1.6" fill="none"/><line x1="0" y1="43" x2="44" y2="43" stroke="rgba(255,255,255,.4)"/></svg>
  </div>
  <div class="abs arrows-line"></div>
</header>

<section class="abs services">
</section>
<div class="abs service" style="left:70px"><div class="service-head"><span class="service-num">01</span><span class="service-rule"></span><span class="caps service-name">Architecture</span></div><p>Cras mollis turpis a ipsum ultes, nec cond imentum ipsum consequat.</p></div>
<div class="abs service" style="left:361px"><div class="service-head"><span class="service-num">02</span><span class="service-rule"></span><span class="caps service-name">Interior</span></div><p>Cras mollis turpis a ipsum ultes, nec cond imentum ipsum consequat.</p></div>
<div class="abs service" style="left:654px"><div class="service-head"><span class="service-num">03</span><span class="service-rule"></span><span class="caps service-name">3D Modeling</span></div><p>Cras mollis turpis a ipsum ultes, nec cond imentum ipsum consequat.</p></div>

<section>
  <div class="abs caps about-label">About us</div>
  <h2 class="abs about-title">Best Interior<br>Designers For You.</h2>
  <p class="abs about-copy">Architecture bibendum pharetra eleifend. Suspendisse vel volutpat purus, sit amet bibendum nisl. Cras mollis turpis a ipsum ultes, nec condimentum ipsum consequat. Mauris vitae consequat nibh, vitae interdum mi.</p>
  <div class="abs about-tags"><span>ARCHITECTURE</span><span>INTERIOR DESIGN</span><span>FURNITURE</span></div>
  <div class="abs btn">Read More</div>
  <div class="abs photo-a" role="img" aria-label="Dining room with yellow chairs and warm cove lighting"></div>
  <div class="abs photo-b" role="img" aria-label="Bright home office corner with plant and arched window"></div>
  <div class="abs exp-box"></div>
  <div class="abs exp-num">21</div>
  <div class="abs caps exp-label">Years of experience</div>
</section>

<section class="abs portfolio"></section>
<div class="abs filter"><span class="on">ALL</span><i></i><span>RESIDENTIAL</span><i></i><span>COMMERCIAL</span><i></i><span>RESTAURANT</span></div>

<div class="abs" style="left:209px;top:1522px;width:352px;height:263px;background:linear-gradient(135deg,#cfc3b3,#9a8a74 60%,#d6b46a)" role="img" aria-label="Townhouse dining room with yellow chairs"></div>
<div class="abs" style="left:639px;top:1522px;width:351px;height:234px;background:linear-gradient(180deg,#e9e6e1,#3a3c40 45%,#c49a63 60%,#4d5563)" role="img" aria-label="Modern kitchen with dark cabinets and wood counter"></div>
<div class="abs port-line"></div>
<div class="abs caps work-title" style="left:209px;top:1804px">Modern Townhouse</div>
<div class="abs caps work-sub" style="left:209px;top:1832px">Architecture , Modern</div>
<div class="abs caps work-title" style="left:639px;top:1775px">Modern Townhouse</div>
<div class="abs caps work-sub" style="left:639px;top:1803px">Architecture , Modern</div>

<div class="abs" style="left:209px;top:1930px;width:352px;height:197px;background:linear-gradient(135deg,#bdb8b0,#6f6c68 50%,#2a2a2a)" role="img" aria-label="Living room with black leather sofas and gabled window"></div>
<div class="abs" style="left:639px;top:1901px;width:351px;height:233px;background:linear-gradient(135deg,#f0eeea,#cfcac2 55%,#b08a5a)" role="img" aria-label="Bright dining area with white chairs and wood table"></div>
<div class="abs caps work-title" style="left:209px;top:2146px">Modern Townhouse</div>
<div class="abs caps work-sub" style="left:209px;top:2174px">Architecture , Modern</div>
<div class="abs caps work-title" style="left:639px;top:2153px">Modern Townhouse</div>
<div class="abs caps work-sub" style="left:639px;top:2181px">Architecture , Modern</div>

<section>
  <div class="abs map" role="img" aria-label="Map of the studio location"></div>
  <h3 class="abs contact-title">Contact Info.</h3>
  <div class="abs caps contact-kicker">Let's talk.</div>
  <div class="abs caps contact-line" style="top:2490px">Email@example.com</div>
  <div class="abs caps contact-line" style="top:2535px">+4.930.555.0192</div>
  <div class="abs caps contact-head">Visit us.</div>
  <div class="abs caps contact-line" style="top:2616px;line-height:22px">148 Larkvale Lane Suite 210,<br>Melbourne, Australia</div>
  <div class="abs contact-social"><span></span><span></span><span></span><span></span></div>
</section>

<footer>
  <div class="abs footer"></div>
  <div class="abs brand foot-brand">Dwellora</div>
  <p class="abs foot-copy">Transforming homes into personalized dream spaces.</p>
  <div class="abs foot-social"><span></span><span></span><span></span><span></span></div>

  <div class="abs foot-head" style="left:418px">USEFUL LINKS</div>
  <ul class="abs foot-list" style="left:418px;top:2877px"><li>Interior Design</li><li>About Us</li><li>Our Portfolio</li><li>Contact Us</li></ul>

  <div class="abs foot-head" style="left:637px">CONTACT US</div>
  <div class="abs foot-text" style="left:637px;top:2881px">
    <svg width="10" height="10" viewBox="0 0 10 10" style="vertical-align:middle;margin-right:6px"><rect x="2" y="0.5" width="6" height="9" rx="1" stroke="#b39a7b" fill="none"/></svg>+7(555)010-2468</div>
  <div class="abs foot-text" style="left:637px;top:2914px">
    <svg width="10" height="10" viewBox="0 0 10 10" style="vertical-align:middle;margin-right:6px"><path d="M1 2c1 4 3 6 7 7l1-2-2-1-1 1C4 6 3.5 5 3 4l1-1-1-2z" fill="#b39a7b"/></svg>+1(555)013-5790</div>
  <div class="abs foot-text" style="left:637px;top:2956px">contact@velmara.com</div>
  <div class="abs foot-text" style="left:637px;top:2988px">studio@dwellora-mail.com</div>

  <div class="abs foot-head" style="left:859px">VISIT</div>
  <div class="abs foot-text" style="left:859px;top:2881px;line-height:30px">42 Ashdown Row,<br>London, Greater London<br>NW4 7QL, United Kingdom</div>

  <div class="abs foot-bottom" style="left:155px">© 2022,Dwellora Made with passion by <b>Studio Kestrel.</b></div>
  <div class="abs foot-nav"><span>Home</span><i></i><span>Policy</span><i></i><span>FAQ</span></div>
</footer>

</body>
</html>
```